VORLEN Website Design

We need a website designed for our company VORLEN. We are a luxury lifestyle club that will provide benefits and services for our members. The site should be clean & sleek, preferably using black and white (or darker colors). (example sites: brimvale.example, tusko.example)

Here is a link of a sample page I did using wix. (https://pelmundry4.sitebuild.example/mypage) This can be used to get a general idea.

Target Market(s)

Upper Middle Class in the United States

Number of Pages Required

5+ page

Font styles to use
Sans Serif
Other font styles liked:
• Arial (or other similar fonts)

Requirements
Must have
• A clean design that is eye-catching and speaks to our company.
Nice to have
• Ideas for copy.

```html
<!DOCTYPE html>
<html lang="en">
<head>
<meta charset="utf-8">
<title>VORLEN — A Members Only Lifestyle Club</title>
<link rel="stylesheet" href="https://fonts.googleapis.com/css2?family=Montserrat:wght@400;500;600&family=Roboto:wght@400;500&display=swap">
<style>
  :root {
    --nav-bg: #232323;
    --accent: #1ab8ea;
    --white: #ffffff;
    --nav-text: #d6d6d6;
    --hero-dark: #3a3a3a;
    --enquiry-bg: #58595b;
    --muted: #6a6a6a;
  }
  * { margin: 0; padding: 0; box-sizing: border-box; }
  html, body { width: 1200px; height: 589px; overflow: hidden; background: var(--white); }
  body { font-family: "Roboto", Arial, sans-serif; position: relative; }

  .site-header {
    position: absolute; top: 0; left: 0; width: 1200px; height: 53px;
    background: var(--nav-bg); display: flex; align-items: center;
  }
  .brand {
    position: absolute; left: 132px; top: 13px;
    font-family: "Montserrat", sans-serif; font-weight: 400; font-size: 22px;
    color: var(--white); letter-spacing: 0.5px;
  }
  .main-nav {
    position: absolute; right: 132px; top: 0; height: 53px;
    display: flex; align-items: center; font-size: 13px; color: var(--nav-text);
  }
  .main-nav a { color: var(--nav-text); text-decoration: none; margin-right: 26px; }
  .main-nav a.is-active { color: var(--accent); }
  .nav-divider { width: 1px; height: 14px; background: #555; margin-right: 16px; margin-left: -10px; }
  .nav-phone { display: flex; align-items: center; color: var(--white); font-weight: 500; font-size: 13.5px; margin-right: 15px; }
  .nav-phone svg { margin-right: 7px; }
  .apply-button {
    background: var(--accent); color: var(--white); font-size: 11px; font-weight: 500;
    padding: 0 16px; height: 27px; display: flex; align-items: center; letter-spacing: 0.3px;
  }

  .hero-left {
    position: absolute; left: 0; top: 53px; width: 600px; height: 445px;
    background: linear-gradient(135deg, #4a4440 0%, #3b3633 45%, #2e2e30 100%);
  }
  .hero-right {
    position: absolute; left: 600px; top: 53px; width: 600px; height: 445px;
    background: linear-gradient(140deg, #2a3f55 0%, #1f3a5a 35%, #6b5040 60%, #1c2230 100%);
  }
  .hero-copy { position: absolute; left: 133px; top: 336px; color: var(--white); font-family: "Montserrat", sans-serif; }
  .hero-kicker { font-size: 25px; font-weight: 500; letter-spacing: 0.5px; }
  .hero-title { font-size: 37px; font-weight: 600; line-height: 43px; letter-spacing: 1px; margin-top: 8px; }

  .enquiry-band {
    position: absolute; left: 0; top: 498px; width: 600px; height: 68px;
    background: var(--enquiry-bg); color: var(--white);
    font-family: "Montserrat", sans-serif; font-size: 18px;
    display: flex; align-items: center; padding-left: 135px;
  }
  .enquiry-band strong { font-weight: 600; margin-left: 5px; }
  .apply-link {
    position: absolute; left: 639px; top: 520px; display: flex; align-items: center;
    font-size: 11.5px; color: var(--muted);
  }
  .apply-link .arrow-circle {
    width: 29px; height: 29px; border-radius: 50%; background: var(--accent);
    display: flex; align-items: center; justify-content: center; margin-right: 8px;
  }
</style>
</head>
<body>
  <header class="site-header">
    <div class="brand">VORLEN</div>
    <nav class="main-nav">
      <a class="is-active">Home</a>
      <a>About</a>
      <a>Services &amp; Benefits</a>
      <a>Contact</a>
      <span class="nav-divider"></span>
      <span class="nav-phone">
        <svg width="14" height="14" viewBox="0 0 24 24"><path fill="#1ab8ea" d="M6.6 10.8a15.1 15.1 0 0 0 6.6 6.6l2.2-2.2c.3-.3.7-.4 1-.2 1.1.4 2.3.6 3.6.6.6 0 1 .4 1 1V20c0 .6-.4 1-1 1A17 17 0 0 1 3 4c0-.6.4-1 1-1h3.5c.6 0 1 .4 1 1 0 1.3.2 2.5.6 3.6.1.3 0 .7-.2 1z"/></svg>
        123-456-7890
      </span>
      <span class="apply-button">APPLY NOW</span>
    </nav>
  </header>

  <div class="hero-left" role="img" aria-label="Dimmed photo of smiling club members socialising"></div>
  <div class="hero-right" role="img" aria-label="Photo of friends laughing and toasting with champagne glasses at a club"></div>

  <div class="hero-copy">
    <div class="hero-kicker">VORLEN</div>
    <h1 class="hero-title">A MEMBERS ONLY<br>LIFESTYLE CLUB</h1>
  </div>

  <div class="enquiry-band">Call for enquiry : <strong>123-456-7890</strong></div>

  <div class="apply-link">
    <span class="arrow-circle">
      <svg width="13" height="13" viewBox="0 0 14 14"><path d="M2 7h9M7.5 3l4 4-4 4" stroke="#fff" stroke-width="2" fill="none" stroke-linecap="round" stroke-linejoin="round"/></svg>
    </span>
    Apply Now
  </div>
</body>
</html>
```